Business Card Design Project

I would like to get a logo as well as business card and stationery.

i am in an event planner and coordination business. I need something sophisticated and elegant.

Business

```html
<!DOCTYPE html>
<html lang="en">
<head>
<meta charset="utf-8">
<title>Linden Occasions · Stationery</title>
<link href="https://fonts.googleapis.com/css2?family=Josefin+Sans:wght@400&family=Questrial&display=swap" rel="stylesheet">
<style>
  :root {
    --brand: #1a8f86;
    --rule: #7fc4bd;
    --ink-light: #9aa3a2;
    --paper: #ffffff;
    --backdrop: #eee8de;
    --edge: #dcd6cc;
  }
  html, body { margin: 0; padding: 0; overflow: hidden; }
  .canvas {
    position: relative; width: 1200px; height: 900px; overflow: hidden;
    background: var(--backdrop);
    font-family: "Questrial", sans-serif;
  }
  .sheet { position: absolute; background: var(--paper); border: 1px solid var(--edge); box-sizing: border-box; }
  .rule { position: absolute; height: 2px; background: var(--rule); }
  .wordmark {
    position: absolute; margin: 0; color: var(--brand);
    font-family: "Josefin Sans", sans-serif; font-weight: 400;
    letter-spacing: 1px; white-space: nowrap;
  }
  .small { position: absolute; margin: 0; color: var(--ink-light); font-size: 9px; line-height: 12px; white-space: nowrap; }
  .small .label { color: var(--brand); }
  .link { color: var(--brand); }

  .brand-tag { position: absolute; left: 0; top: 0; width: 540px; height: 80px; background: var(--paper); }
  .brand-tag h1 {
    margin: 0; position: absolute; left: 20px; top: 16px;
    font-family: "Josefin Sans", sans-serif; font-weight: 400; font-size: 44px;
    letter-spacing: 1px; color: var(--brand); white-space: nowrap;
  }
  .web-tag { position: absolute; left: 0; top: 816px; width: 444px; height: 84px; background: var(--paper); }
  .web-tag p {
    margin: 0; position: absolute; left: 30px; top: 30px;
    font-family: "Josefin Sans", sans-serif; font-weight: 400; font-size: 26px;
    letter-spacing: 2px; color: var(--brand); white-space: nowrap;
  }

  .letterhead { left: 540px; top: -2px; width: 680px; height: 858px; }
  .envelope { left: 412px; top: 236px; width: 700px; height: 304px; }
  .card-front { left: 406px; top: 580px; width: 256px; height: 144px; }
  .card-back { left: 686px; top: 580px; width: 256px; height: 144px; }
  .person { position: absolute; left: 14px; top: 22px; margin: 0; color: var(--brand); font-size: 15px; }
  .role { position: absolute; left: 14px; top: 40px; margin: 0; color: var(--brand); font-size: 9px; }
</style>
</head>
<body>
<div class="canvas">

  <div class="sheet letterhead">
    <div class="rule" style="left:26px;top:46px;width:40px"></div>
    <h2 class="wordmark" style="left:26px;top:100px;font-size:21px">Linden Occasions</h2>
    <p class="small" style="left:26px;top:740px">Linden Occasions Ltd<br>Harlow House<br>12 Bank Street<br>Brookfield<br>NW4 3RT<br>United Kingdom</p>
    <p class="small" style="left:146px;top:740px"><span class="label">Telephone</span><br>01 2345 6789<br><br><span class="label">Facsimile</span><br>01 2345 6780</p>
    <p class="small" style="left:146px;top:804px"><span class="link">www.lindenoccasions.com</span></p>
  </div>

  <div class="sheet envelope">
    <div class="rule" style="left:30px;top:30px;width:40px"></div>
    <h2 class="wordmark" style="left:30px;top:58px;font-size:21px">Linden Occasions</h2>
    <p class="small" style="left:30px;top:200px">Linden Occasions Ltd<br>Harlow House<br>12 Bank Street<br>Brookfield<br>NW4 3RT<br>United Kingdom</p>
    <p class="small" style="left:150px;top:200px"><span class="label">Telephone</span><br>01 2345 6789<br><br><span class="label">Facsimile</span><br>01 2345 6780</p>
    <p class="small" style="left:150px;top:262px"><span class="link">www.lindenoccasions.com</span></p>
  </div>

  <div class="sheet card-front">
    <p class="person">Alex Marlow</p>
    <p class="role">Senior Vice President</p>
    <p class="small" style="left:14px;top:62px;font-size:7px;line-height:10px">Harlow House<br>12 Bank Street<br>Brookfield, NW4 3RT</p>
    <p class="small" style="left:120px;top:62px;font-size:7px;line-height:10px">alex@lindenoccasions.com</p>
    <p class="small" style="left:14px;top:98px;font-size:7px;line-height:10px">Tel 01 2345 6789<br>Fax 01 2345 6780</p>
    <p class="small" style="left:120px;top:98px;font-size:7px;line-height:10px"><span class="link">www.lindenoccasions.com</span></p>
  </div>

  <div class="sheet card-back">
    <div class="rule" style="left:24px;top:82px;width:30px"></div>
    <h2 class="wordmark" style="left:24px;top:92px;font-size:15px">Linden Occasions</h2>
  </div>

  <div class="brand-tag"><h1>Linden Occasions</h1></div>
  <div class="web-tag"><p>www.lindenoccasions.com</p></div>

</div>
</body>
</html>
```